RAmio Shop Business Card Design

My auto shop is targeted to the European and Asian luxury automotive market. We do mechanics collision and parts.
Some of the makes are KTR, DQ, Stone Herald, Valdine,Norvi, solavanta, bremo, HJ, etc. But in the end we get all makes.
I don't want to have the makes logos on the business card.
The Name of the business is after my first Name Ramiro but without the s Ramio Shop if there is any other ideas about the name iam open to suggestions. And i don't have a LOGO. Need logo!
Updates

Reason: I increased my budget and invited more designers. And committed payment so giving you guys more time.

Target Market(s)

target is the luxury auto market

Industry/Entity Type

Automotive

Contact Information for Business Card

European Automotive Repair Shop, Collision Mechanics Parts
Ramiro Villalba Owner, Colibrí #14 Loma Serena 2

Requirements
Nice to have
• One design i can of liked was the use of the dash error logos like check engine light airbag light. Nobla press has this but dose not include the air bag light. For the collision part of the business. But am open to any design.
Should not have
• exact logo makes on front of card.

```html
<!DOCTYPE html>
<html lang="en">
<head>
<meta charset="utf-8">
<title>RAmio Shop Business Card</title>
<link rel="stylesheet" href="https://fonts.googleapis.com/css2?family=Open+Sans:ital,wght@0,400;0,700;1,700&display=swap">
<style>
  :root {
    --bg: #d9d9d9;
    --paper: #ffffff;
    --charcoal: #3b3b3b;
    --ink: #1f1f1f;
    --amber: #f5b43c;
  }
  * { box-sizing: border-box; margin: 0; padding: 0; }
  html, body {
    width: 1200px; height: 1012px; overflow: hidden;
    background: var(--bg);
    font-family: "Open Sans", Arial, sans-serif;
  }
  .sheet {
    width: 1200px; height: 1012px;
    display: flex; flex-direction: column; align-items: center; justify-content: center;
    gap: 28px;
  }
  .card {
    position: relative;
    width: 820px; height: 468px;
    background: var(--paper);
    overflow: hidden;
    box-shadow: 0 4px 14px rgba(0,0,0,.18);
  }
  .brand {
    position: absolute;
    left: 0; right: 0;
    display: flex; align-items: center; justify-content: center; gap: 18px;
    color: var(--ink);
    font-weight: 700;
    letter-spacing: 1px;
    line-height: 1;
    white-space: nowrap;
  }
  .brand-square {
    width: 46px; height: 46px;
    background: var(--ink);
    flex: none;
  }
  /* Front */
  .front .brand { top: 140px; font-size: 78px; }
  .front .band {
    position: absolute; left: 0; right: 0; bottom: 0; height: 124px;
    background: var(--charcoal);
    display: flex; align-items: center; padding-left: 44px;
  }
  .slogan {
    font-style: italic; font-weight: 700; color: var(--amber);
    font-size: 34px;
    white-space: nowrap;
  }
  /* Back */
  .back .brand { top: 50px; font-size: 62px; }
  .back .brand .brand-square { width: 40px; height: 40px; }
  .back .panel {
    position: absolute; left: 0; right: 0; top: 168px; bottom: 0;
    background: var(--charcoal);
  }
  .back .rule {
    position: absolute; top: 22px; left: 36px; right: 36px; height: 3px;
    background: var(--amber);
  }
  .back .services {
    position: absolute; top: 8px; left: 50%; transform: translateX(-50%);
    background: var(--charcoal); padding: 0 14px;
    font-style: italic; font-weight: 700; color: var(--amber); font-size: 21px;
    line-height: 32px;
    white-space: nowrap;
  }
  .contact {
    position: absolute; left: 40px; top: 62px;
    list-style: none; color: var(--paper);
  }
  .contact li { display: flex; align-items: center; gap: 12px; margin-bottom: 10px; white-space: nowrap; }
  .contact .name { font-size: 26px; }
  .contact .detail { font-size: 17px; }
  .contact svg { fill: var(--amber); flex: none; }
  .dash-lights {
    position: absolute; right: 36px; top: 60px;
    width: 400px; height: 150px;
    background: linear-gradient(135deg, #545454, #444);
    border-radius: 6px;
  }
  .back .strip {
    position: absolute; left: 0; bottom: 40px; width: 470px; height: 50px;
    background: var(--amber);
    clip-path: polygon(0 0, 100% 0, 94% 100%, 0 100%);
    display: flex; align-items: center; padding-left: 28px;
  }
  .back .strip .slogan { color: var(--charcoal); font-size: 26px; }
  .back .tail {
    position: absolute; right: 0; bottom: 0; width: 380px; height: 40px;
    background: var(--amber);
    clip-path: polygon(8% 0, 100% 0, 100% 100%, 0 100%);
  }
  .back .base {
    position: absolute; left: 0; right: 0; bottom: 0; height: 40px;
    background: var(--paper);
  }
</style>
</head>
<body>
<main class="sheet">
  <section class="card front">
    <div class="brand"><span class="brand-square"></span><span>RAmio Shop</span></div>
    <div class="band"><p class="slogan">European Automotive Repair Shop</p></div>
  </section>

  <section class="card back">
    <div class="brand"><span class="brand-square"></span><span>RAmio Shop</span></div>
    <div class="panel">
      <div class="rule"></div>
      <p class="services">Collision Mechanics Parts Ramiro Villalba Owner</p>
      <ul class="contact">
        <li class="name">
          <svg width="26" height="26" viewBox="0 0 24 24"><circle cx="12" cy="7" r="5"/><path d="M2 23c0-6 4.5-9 10-9s10 3 10 9z"/></svg>
          Maestro R
        </li>
        <li class="detail">
          <svg width="20" height="20" viewBox="0 0 24 24"><path d="M6.6 10.8a15 15 0 0 0 6.6 6.6l2.2-2.2c.3-.3.7-.4 1-.2 1.1.4 2.3.6 3.6.6.6 0 1 .4 1 1V20c0 .6-.4 1-1 1A17 17 0 0 1 3 4c0-.6.4-1 1-1h3.5c.6 0 1 .4 1 1 0 1.3.2 2.5.6 3.6.1.3 0 .7-.2 1z"/></svg>
          456 555 0148
        </li>
        <li class="detail">
          <svg width="22" height="20" viewBox="0 0 24 22"><path d="M12 1 1 11h3v10h6v-6h4v6h6V11h3z"/></svg>
          Colibrí #14 Loma Serena 2
        </li>
      </ul>
      <div class="dash-lights" role="img" aria-label="Grid of dashboard warning light icons: check engine, oil, battery, warning triangle, coolant, defrost, turn signals, tyre pressure, ABS, brake, airbag, traction and headlight"></div>
    </div>
    <div class="base"></div>
    <div class="tail"></div>
    <div class="strip"><p class="slogan">European Automotive Repair Shop</p></div>
  </section>
</main>
</body>
</html>
```